Web Design - 1 page for Buy - Repair - Service - Upgrade - PC Maintenance

We specialize in consumer and small business. It will be mobile friendly, viewable on all devices. Fully editable at the text level of the sections !!! - HTML / CSS only to be able to add a section would be to the web site
Updates

Target Market(s)

consumer and small business IT.

Coding

Coded - Design and coding required

Number of Pages Required

1 page

Font styles to use
Sans Serif

Requirements
Must have
• Looking for a page with a design that compliments the business card and pamphlet that has already been made (attached files). It should look professional and easy to read business. Email and phone number should be visible when the page loads. I do not want any forms for people to mess with. No "Contact Us" form or enter in email for newsletter. Customers will just be looking for this site to confirm we are professionals and have our business in order. OpenStreetMap: embedding map in webpage (like Google Maps) to where the workshop is located
Nice to have
• 2vask.com => this style of website would be more modern visually by integrating higher demands

```html
<!DOCTYPE html>
<html lang="en">
<head>
<meta charset="utf-8">
<title>Northvale Tech — Computer Repair &amp; Service</title>
<link href="https://fonts.googleapis.com/css2?family=IBM+Plex+Sans:wght@400;500;600&display=swap" rel="stylesheet">
<style>
  :root {
    --brand-blue: #0a8bd9;
    --white: #ffffff;
    --soft-text: #a9d6f3;
    --heading-dark: #1b1b1b;
    --body-gray: #8a8a8a;
    --badge-green: #79c96f;
    --badge-green-soft: #8fd486;
    --contact-text: #e9ecef;
  }
  * { box-sizing: border-box; margin: 0; padding: 0; }
  html, body {
    width: 1200px; height: 1000px; overflow: hidden;
    font-family: "IBM Plex Sans", Arial, sans-serif;
    background: var(--white);
  }
  .page { position: relative; width: 1200px; height: 1000px; overflow: hidden; }
  .top-bar { position: absolute; top: 0; left: 0; width: 1200px; height: 6px; background: var(--brand-blue); z-index: 3; }
  .hero { position: absolute; top: 0; left: 0; width: 1200px; height: 810px; }
  .hero-art { position: absolute; inset: 0; }
  .brand {
    position: absolute; left: 135px; top: 240px;
    display: flex; align-items: center; gap: 12px;
    color: var(--white); font-size: 40px; font-weight: 600; letter-spacing: 0.3px;
  }
  .brand-mark { width: 18px; height: 18px; background: var(--white); }
  .contact { position: absolute; left: 538px; top: 198px; list-style: none; }
  .contact li {
    display: flex; align-items: center; gap: 34px;
    color: var(--contact-text); font-size: 39px; font-weight: 500; height: 54px;
  }
  .contact svg { width: 34px; height: 34px; flex: none; }
  .honest-badge {
    position: absolute; left: 550px; top: 470px; width: 100px; height: 112px;
    border-radius: 8px;
    background: linear-gradient(90deg, var(--badge-green) 0%, var(--badge-green-soft) 100%);
  }
  .honest {
    position: absolute; top: 612px; left: 0; width: 1200px; text-align: center;
  }
  .honest h2 { color: var(--white); font-size: 34px; font-weight: 600; margin-bottom: 16px; }
  .honest p {
    width: 880px; margin: 0 auto; color: var(--soft-text);
    font-size: 20px; line-height: 30px;
  }
  .service {
    position: absolute; top: 810px; left: 0; width: 1200px; height: 190px;
  }
  .service-copy { position: absolute; left: 135px; top: 72px; width: 668px; }
  .service-copy h3 { color: var(--heading-dark); font-size: 28px; font-weight: 500; margin-bottom: 16px; }
  .service-copy p { color: var(--body-gray); font-size: 19px; line-height: 30px; }
  .service-art {
    position: absolute; left: 850px; top: 75px; width: 215px; height: 140px;
    background: radial-gradient(circle at 50% 90%, #f4d9a8 0%, #f6e9d2 45%, #ffffff 75%);
  }
</style>
</head>
<body>
<main class="page">
  <div class="top-bar"></div>

  <section class="hero">
    <svg class="hero-art" width="1200" height="810" viewBox="0 0 1200 810">
      <defs>
        <linearGradient id="photoTone" x1="0" y1="0" x2="1" y2="1">
          <stop offset="0" stop-color="#2b3946"/>
          <stop offset="0.5" stop-color="#3a4854"/>
          <stop offset="1" stop-color="#1e2b37"/>
        </linearGradient>
      </defs>
      <rect x="0" y="0" width="1200" height="520" fill="url(#photoTone)" role="img" aria-label="Photo of students working at desktop computers in a computer lab"/>
      <polygon points="0,395 600,517 1200,395 1200,810 0,810" fill="var(--brand-blue)"/>
    </svg>

    <div class="brand"><span>Northvale Tech</span><span class="brand-mark"></span></div>

    <ul class="contact">
      <li>
        <svg viewBox="0 0 34 34"><rect x="1" y="5" width="32" height="24" rx="3" fill="var(--contact-text)"/><path d="M3 8 L17 18 L31 8" fill="none" stroke="#2d3b48" stroke-width="2.5"/></svg>
        help@northvaletech.com
      </li>
      <li>
        <svg viewBox="0 0 34 34"><path d="M8 2 L13 2 L16 10 L12 13 C14 18 16 21 21 23 L24 19 L32 22 L32 27 C32 30 30 32 27 32 C13 31 3 21 2 7 C2 4 4 2 8 2 Z" fill="var(--contact-text)"/></svg>
        555-014-2290
      </li>
    </ul>

    <div class="honest-badge" role="img" aria-label="Green shield illustration symbolising trusted, honest service"></div>

    <div class="honest">
      <h2>Honest Service</h2>
      <p>Our certified technicians aren't paid on commission. No pressure to upgrade to products/services you don't need or want. Even the best computers will eventually break down, and if we leave you happy, that's when we hope you'll come back to us.</p>
    </div>
  </section>

  <section class="service">
    <div class="service-copy">
      <h3>Malware/Virus Removal</h3>
      <p>Infections can come from many places and sometimes antivirus just isn't enough. We can get your system back to top shape, and train users how to avoid future threats.</p>
    </div>
    <div class="service-art" role="img" aria-label="Illustration of a crossed-out bug symbolising virus removal"></div>
  </section>
</main>
</body>
</html>
```